Veterinary Pylon

My veterinary clinic is not clearly visible from the street and I want to place a Pylon next to my driveway. I want a modern, elegant straight Design, the Photo shows the sheduled place. One can see the clinic on our Homepage: www.fernhollow-tierpraxis.at
The last pictures are examples for pylones I like

Target Market(s)

the passing cars often miss my entry...I want to show where to turn left

Colors
3276b5
33a6d7
00a990

Requirements
Must have
• High value, simple elegance, size: 250cm (high) x 100cm (width)
Nice to have
• Our Logo, arrow(?)

A special Text is not necessary but this will be an option:

Biegen sie hier ab und wir biegen es wieder hin!
Should not have
• Too much Color, the colors I have chosen are the possible colors but it‘s not necessary to use them.

```html
<!DOCTYPE html>
<html lang="de">
<head>
<meta charset="utf-8">
<title>Fernhollow Tierpraxis – Pylon</title>
<link rel="stylesheet" href="https://fonts.googleapis.com/css2?family=Source+Sans+3:wght@600;700&display=swap">
<style>
  :root {
    --navy: #124b92;
    --teal: #16ab94;
    --sky: #2fb8e0;
    --white: #ffffff;
  }
  html, body {
    margin: 0;
    padding: 0;
    width: 1200px;
    height: 3000px;
    overflow: hidden;
    background: var(--white);
  }
  .pylon {
    position: relative;
    width: 1200px;
    height: 3000px;
    overflow: hidden;
    background: var(--white);
    font-family: "Source Sans 3", "Myriad Pro", Arial, sans-serif;
  }
  .pylon__waves {
    position: absolute;
    inset: 0;
    width: 1200px;
    height: 3000px;
  }
  .wave--navy { fill: var(--navy); }
  .wave--teal { fill: var(--teal); }
  .turn-arrow { fill: var(--white); }

  .brand {
    position: absolute;
    display: flex;
    align-items: center;
    gap: 48px;
  }
  .brand--header {
    left: 90px;
    top: 150px;
  }
  .brand__dot {
    flex: none;
    width: 190px;
    height: 190px;
    border-radius: 50%;
    background: var(--sky);
  }
  .brand__name {
    margin: 0;
    font-weight: 700;
    font-size: 118px;
    line-height: 1.0;
    letter-spacing: 1px;
    color: var(--navy);
  }
  .brand--footer {
    left: 0;
    right: 0;
    top: 2330px;
    justify-content: center;
  }
  .brand--footer .brand__dot {
    width: 170px;
    height: 170px;
    background: var(--white);
  }
  .brand--footer .brand__name {
    color: var(--white);
    font-size: 112px;
  }

  .slogan {
    position: absolute;
    left: 0;
    right: 0;
    top: 1505px;
    margin: 0;
    text-align: center;
    font-weight: 600;
    font-size: 104px;
    line-height: 128px;
    color: var(--white);
  }
</style>
</head>
<body>
<main class="pylon">
  <svg class="pylon__waves" viewBox="0 0 1200 3000" aria-hidden="true">
    <path class="wave--navy" d="M1200,403 C1000,400 880,560 760,700 C680,790 600,860 531,883 L0,900 L0,3000 L1200,3000 Z"/>
    <path class="wave--teal" d="M0,771 C200,770 420,820 531,883 C800,1030 1000,1230 1157,1397 C1000,1280 750,1170 480,1180 C280,1190 120,1230 0,1286 Z"/>
    <path class="turn-arrow" d="M843,835 L910,771 L955,771 L905,818 L1083,818 L1083,853 L905,853 L955,900 L910,900 Z"/>
  </svg>

  <header class="brand brand--header">
    <span class="brand__dot"></span>
    <h1 class="brand__name">Fernhollow<br>Tierpraxis</h1>
  </header>

  <p class="slogan">Biegen sie hier ab<br>und wir biegen es<br>wieder hin!</p>

  <footer class="brand brand--footer">
    <span class="brand__dot"></span>
    <p class="brand__name">Fernhollow<br>Tierpraxis</p>
  </footer>
</main>
</body>
</html>
```